Business Card Design Project

We need business cards for the new company Venture Loom based in Abu Dhabi, UAE, which provides IT retail solutions to businesses
Design should be done as a template, so we can add people when needed.
Please see attached details.
The brief is about 2 companies from our group. We need a business card only for Venture Loom
Industry/Entity Type
Retail
Look and feel
Each slider illustrates characteristics of the customer's brand and the style your logo design should communicate.

```html
<!DOCTYPE html>
<html lang="en">
<head>
<meta charset="utf-8">
<title>Venture Loom – Business Cards</title>
<link href="https://fonts.googleapis.com/css2?family=Tinos:wght@400;700&family=Noto+Naskh+Arabic:wght@400;700&display=swap" rel="stylesheet">
<style>
  :root {
    --purple: #7b2a8e;
    --purple-dark: #5e1b70;
    --gold: #d9b23a;
    --gold-light: #f3dc7a;
    --ink: #2b2b2b;
    --grey: #555;
    --card: #fbfbfb;
    --stage: #d9d9d9;
  }
  * { box-sizing: border-box; margin: 0; padding: 0; }
  html, body { width: 1200px; height: 900px; overflow: hidden; }
  body { background: var(--stage); position: relative; font-family: "Tinos", "Times New Roman", serif; }

  .card {
    position: absolute;
    width: 540px; height: 310px;
    background: var(--card);
    border-radius: 10px;
    overflow: hidden;
    box-shadow: 0 10px 28px rgba(0,0,0,.22);
  }
  .card--front { left: 60px; top: 130px; }
  .card--back  { left: 600px; top: 460px; }

  .card__band { position: absolute; left: 0; bottom: 0; width: 540px; height: 310px; }

  .brand {
    position: absolute;
    display: flex; align-items: center; gap: 10px;
    color: var(--purple);
    font-family: "Tinos", "Times New Roman", serif;
    font-weight: 700;
    font-size: 34px;
    letter-spacing: .5px;
  }
  .brand__dot { width: 16px; height: 16px; border-radius: 50%; background: var(--gold); }
  .card--front .brand { left: 34px; top: 120px; }
  .card--back .brand { left: 40px; top: 46px; }

  .details { position: absolute; color: var(--grey); font-size: 13px; line-height: 20px; }
  .card--front .details { right: 28px; top: 26px; text-align: right; }
  .details__name { color: var(--ink); font-weight: 700; font-size: 19px; line-height: 24px; }
  .details__title { color: var(--purple); font-size: 13.5px; margin-bottom: 8px; }
  .details__row { display: flex; justify-content: flex-end; align-items: center; gap: 8px; }
  .badge {
    width: 15px; height: 15px; border-radius: 50%;
    border: 1px solid var(--purple); color: var(--purple);
    font-size: 9px; line-height: 13px; text-align: center; font-weight: 700;
    background: #f1e6f4;
  }
  .details__spacer { width: 15px; }

  .card--back .details { right: 28px; top: 120px; text-align: right; }
  .details--ar .details__name { font-family: "Noto Naskh Arabic", serif; font-size: 22px; line-height: 30px; }
  .details--ar .details__title, .details--ar .details__addr { font-family: "Noto Naskh Arabic", serif; direction: rtl; }
  .details--ar .details__title { margin-bottom: 2px; }

  .website {
    position: absolute; right: 30px; bottom: 18px;
    color: #fff; font-size: 13px; font-weight: 700; letter-spacing: 3px;
  }
  .card--back .website { left: 30px; right: auto; }
</style>
</head>
<body>

  <section class="card card--front" aria-label="Business card front">
    <svg class="card__band" viewBox="0 0 540 310" aria-hidden="true">
      <path d="M0,272 C170,300 330,250 540,196 L540,310 L0,310 Z" fill="var(--purple)"/>
      <path d="M0,272 C170,300 330,250 540,196" fill="none" stroke="var(--gold)" stroke-width="4"/>
      <path d="M0,278 C170,306 330,256 540,202" fill="none" stroke="var(--gold-light)" stroke-width="1"/>
    </svg>

    <div class="brand"><span class="brand__dot"></span>Venture Loom</div>

    <div class="details">
      <p class="details__name">Karim Haddad</p>
      <p class="details__title">Retail Solutions Manager</p>
      <p class="details__row">PO Box – 51830, Abu Dhabi, UAE <span class="details__spacer"></span></p>
      <p class="details__row">971 2 410 7720 – Ext: 210 <span class="badge">T</span></p>
      <p class="details__row">+971 2 410 7735 <span class="badge">F</span></p>
      <p class="details__row">+971 55 3021846 <span class="badge">M</span></p>
      <p class="details__row">k.haddad@ventureloom.ae <span class="badge">E</span></p>
    </div>

    <p class="website">www.ventureloom.ae</p>
  </section>

  <section class="card card--back" aria-label="Business card back">
    <svg class="card__band" viewBox="0 0 540 310" aria-hidden="true">
      <path d="M0,196 C210,250 370,300 540,272 L540,310 L0,310 Z" fill="var(--purple)"/>
      <path d="M0,196 C210,250 370,300 540,272" fill="none" stroke="var(--gold)" stroke-width="4"/>
      <path d="M0,202 C210,256 370,306 540,278" fill="none" stroke="var(--gold-light)" stroke-width="1"/>
    </svg>

    <div class="brand"><span class="brand__dot"></span>Venture Loom</div>

    <div class="details details--ar" lang="ar">
      <p class="details__name">كريم حداد</p>
      <p class="details__title">مدير حلول التجزئة</p>
      <p class="details__row details__addr">ص.ب ٥١٨٣٠، أبوظبي، الإمارات <span class="details__spacer"></span></p>
      <p class="details__row">971 2 410 7720 – Ext: 210 <span class="badge">T</span></p>
      <p class="details__row">+971 2 410 7735 <span class="badge">F</span></p>
      <p class="details__row">+971 55 3021846 <span class="badge">M</span></p>
      <p class="details__row">k.haddad@ventureloom.ae <span class="badge">E</span></p>
    </div>

    <p class="website">www.ventureloom.ae</p>
  </section>

</body>
</html>
```